I need jar labels, and other types to include round and cigar band with an already designed logo

Need a round sticker to place on products, jar labels, 3 sizes with 1 label having 3 different names. also reflect my design on a thank you card and round sticker
I would like a 10 " cigar band with my logo in the middle for handmade bars of soap

Target Market(s)

This project will be for labeling my products for my e-commerce business

Industry/Entity Type

Beauty

Font styles to use
Serif

Colors
e667a6
ffcf3e

Requirements
Must have
• The labels must contain my logo. I need (4) 1.5" X 4" label with my logo and the words: Handmade Sugar Scrub, Handmade Whipped Body Butter, Handmade Whipped Soap Scrub, Handmade Salt Scrub

I also must have a round sticker 2' in diameter with my logo in Gold

I also need a round sticker I rose gold that reflects my logo and says thank you for supporting my small business.
Nice to have
• I want round and rectangle labels for products that contain my logo. I also need thank you cards and thank you for your order sticker with my logo
Should not have
• do not change the color of my logo and make the print on the labels in Black

```html
<!DOCTYPE html>
<html lang="en">
<head>
<meta charset="utf-8">
<title>Soak and Suds – Label Set</title>
<link rel="stylesheet" href="https://fonts.googleapis.com/css2?family=Montserrat:wght@500&family=Libre+Caslon+Text:wght@400;700&family=Josefin+Sans:wght@300&display=swap">
<style>
  :root {
    --backdrop: #d2d2d2;
    --label-black: #0d0d0d;
    --sticker-dark: #2a2727;
    --gold: #f2cd3e;
    --gold-deep: #b8872b;
    --gold-tint: #f3e6c3;
    --rose: #e8a9a4;
    --ink-grey: #4a4a4a;
    --script-tint: #ececec;
    --cream: #fbf3d3;
    --paper: #ffffff;
  }
  html, body { margin: 0; padding: 0; overflow: hidden; }
  body { background: var(--backdrop); }
  .canvas {
    position: relative;
    width: 701px;
    height: 1200px;
    overflow: hidden;
    background: var(--backdrop);
  }
  .jar-label {
    position: absolute;
    width: 275px;
    height: 103px;
    background: var(--label-black);
    box-shadow: 2px 3px 4px rgba(0,0,0,.35);
  }
  .jar-label svg { position: absolute; inset: 0; }
  .brand-name {
    position: absolute;
    left: 0; right: 0;
    margin: 0;
    text-align: center;
    font-family: "Montserrat", sans-serif;
    font-weight: 500;
    color: var(--gold);
    line-height: 1;
  }
  .jar-label .brand-name { top: 48px; font-size: 8px; }
  .product-kicker {
    position: absolute;
    top: 76px; left: 0; right: 0;
    margin: 0;
    text-align: center;
    font-family: "Libre Caslon Text", serif;
    font-size: 6px;
    letter-spacing: 3.2px;
    color: var(--gold);
    line-height: 1;
  }
  .product-name {
    position: absolute;
    top: 83px; left: 0; right: 0;
    margin: 0;
    text-align: center;
    font-family: "Libre Caslon Text", serif;
    font-weight: 400;
    font-size: 12.5px;
    color: var(--gold);
    line-height: 1;
  }
  .sticker {
    position: absolute;
    width: 216px;
    height: 216px;
    filter: drop-shadow(2px 3px 3px rgba(0,0,0,.3));
  }
  .sticker text { font-family: "Libre Caslon Text", serif; }
  .sticker .ring-heading { font-weight: 700; }
  .sticker .badge-name { font-family: "Montserrat", sans-serif; font-weight: 500; }
  .soap-band { position: absolute; left: 60px; top: 700px; width: 604px; height: 92px; }
  .band-brand { position: absolute; left: 310px; width: 101px; top: 700px; height: 90px; }
  .band-brand .brand-name { top: 42px; font-size: 8px; }
  .thank-you-card {
    position: absolute;
    left: 164px; top: 869px;
    width: 413px; height: 275px;
    background: var(--paper);
    box-shadow: 2px 3px 4px rgba(0,0,0,.3);
  }
  .thank-you-card svg { position: absolute; inset: 0; }
  .card-message {
    position: absolute;
    left: 110px; width: 200px;
    top: 189px;
    margin: 0;
    text-align: center;
    font-family: "Josefin Sans", sans-serif;
    font-weight: 300;
    font-size: 9px;
    line-height: 11.5px;
    color: #333;
  }
</style>
</head>
<body>
<main class="canvas">

  <svg width="0" height="0" style="position:absolute" aria-hidden="true">
    <defs>
      <linearGradient id="gold-sheen" x1="0" y1="0" x2="0" y2="1">
        <stop offset="0" stop-color="#f7dc78"/>
        <stop offset="1" stop-color="#b8872b"/>
      </linearGradient>
      <linearGradient id="rose-sheen" x1="0" y1="0" x2="1" y2="1">
        <stop offset="0" stop-color="#f3c4bd"/>
        <stop offset="1" stop-color="#c77f7a"/>
      </linearGradient>
      <symbol id="label-frame" viewBox="0 0 275 103">
        <rect x="6" y="6" width="263" height="91" fill="none" stroke="#f2cd3e" stroke-width=".6" stroke-dasharray="1 1" opacity=".6"/>
        <path d="M40 90 H10 V10 H266 V90 H236" fill="none" stroke="#f2cd3e" stroke-width="1"/>
        <circle cx="40" cy="90" r="1.7" fill="none" stroke="#f2cd3e" stroke-width=".8"/>
        <circle cx="236" cy="90" r="1.7" fill="none" stroke="#f2cd3e" stroke-width=".8"/>
      </symbol>
    </defs>
  </svg>

  <!-- Jar labels -->
  <article class="jar-label" style="left:64px;top:80px">
    <svg viewBox="0 0 275 103"><use href="#label-frame"/></svg>
    <p class="brand-name">SOAK AND SUDS</p>
    <p class="product-kicker">HANDMADE</p>
    <h2 class="product-name">SUGAR SCRUB</h2>
  </article>
  <article class="jar-label" style="left:361px;top:80px">
    <svg viewBox="0 0 275 103"><use href="#label-frame"/></svg>
    <p class="brand-name">SOAK AND SUDS</p>
    <p class="product-kicker">HANDMADE</p>
    <h2 class="product-name">SALT SCRUB</h2>
  </article>
  <article class="jar-label" style="left:64px;top:202px">
    <svg viewBox="0 0 275 103"><use href="#label-frame"/></svg>
    <p class="brand-name">SOAK AND SUDS</p>
    <p class="product-kicker">HANDMADE</p>
    <h2 class="product-name">WHIPPED SOAP SCRUB</h2>
  </article>
  <article class="jar-label" style="left:361px;top:202px">
    <svg viewBox="0 0 275 103"><use href="#label-frame"/></svg>
    <p class="brand-name">SOAK AND SUDS</p>
    <p class="product-kicker">HANDMADE</p>
    <h2 class="product-name">WHIPPED BODY BUTTER</h2>
  </article>

  <!-- Rose gold round sticker -->
  <svg class="sticker sticker-rose" style="left:112px;top:386px" viewBox="0 0 216 216">
    <circle cx="108" cy="108" r="108" fill="var(--sticker-dark)"/>
    <circle cx="108" cy="108" r="102" fill="none" stroke="url(#rose-sheen)" stroke-width="1" stroke-dasharray="1 1.5"/>
    <circle cx="108" cy="108" r="98" fill="none" stroke="url(#rose-sheen)" stroke-width="1.6"/>
    <path id="rose-top" d="M28 108 A80 80 0 0 1 188 108" fill="none"/>
    <path id="rose-bottom" d="M17 108 A91 91 0 0 0 199 108" fill="none"/>
    <text class="ring-heading" font-size="17" fill="url(#rose-sheen)" letter-spacing="1.5"><textPath href="#rose-top" startOffset="50%" text-anchor="middle">THANK YOU</textPath></text>
    <text font-size="12.5" fill="url(#rose-sheen)" letter-spacing=".4"><textPath href="#rose-bottom" startOffset="50%" text-anchor="middle">FOR SUPPORTING MY SMALL BUSINESS</textPath></text>
    <circle cx="108" cy="108" r="57" fill="none" stroke="url(#rose-sheen)" stroke-width="1.6"/>
    <text class="badge-name" x="108" y="111" font-size="9" text-anchor="middle" fill="var(--rose)">SOAK AND SUDS</text>
  </svg>

  <!-- Gold round sticker -->
  <svg class="sticker sticker-gold" style="left:372px;top:386px" viewBox="0 0 216 216">
    <circle cx="108" cy="108" r="108" fill="var(--paper)"/>
    <circle cx="108" cy="108" r="99" fill="none" stroke="url(#gold-sheen)" stroke-width="2"/>
    <path id="gold-top" d="M28 108 A80 80 0 0 1 188 108" fill="none"/>
    <path id="gold-bottom" d="M22 108 A86 86 0 0 0 194 108" fill="none"/>
    <text class="ring-heading" font-size="17" fill="var(--ink-grey)" letter-spacing="1.5"><textPath href="#gold-top" startOffset="50%" text-anchor="middle">THANK YOU</textPath></text>
    <text font-size="12.5" fill="var(--ink-grey)" letter-spacing=".4"><textPath href="#gold-bottom" startOffset="50%" text-anchor="middle">FOR YOUR ORDER</textPath></text>
    <circle cx="108" cy="108" r="57" fill="none" stroke="url(#gold-sheen)" stroke-width="1.6"/>
    <text class="badge-name" x="108" y="111" font-size="9" text-anchor="middle" fill="var(--gold-deep)">SOAK AND SUDS</text>
  </svg>

  <!-- Soap cigar band -->
  <svg class="soap-band" viewBox="0 0 604 92" style="filter:drop-shadow(2px 3px 3px rgba(0,0,0,.3))">
    <rect x="0" y="16" width="604" height="60" fill="var(--label-black)"/>
    <rect x="250" y="1" width="101" height="89" fill="var(--label-black)"/>
    <path d="M0 21 H255 V6 H346 V21 H604" fill="none" stroke="var(--cream)" stroke-width="1.6"/>
    <path d="M0 71 H255 V85 H346 V71 H604" fill="none" stroke="var(--cream)" stroke-width="1.6"/>
  </svg>
  <div class="band-brand">
    <p class="brand-name">SOAK AND SUDS</p>
  </div>

  <!-- Thank you card -->
  <section class="thank-you-card">
    <svg viewBox="0 0 413 275">
      <path d="M210 13 L317 75 V196 L210 258 L103 196 V75 Z" fill="none" stroke="url(#gold-sheen)" stroke-width="1.2"/>
      <path d="M200 20 L312 68 L322 190 L218 252 L98 204 L108 80 Z" fill="none" stroke="url(#gold-sheen)" stroke-width="1"/>
      <path d="M96 62 Q124 44 160 40 L150 58 Q116 82 110 150 Q108 190 150 214 L132 226 Q86 196 86 140 Q86 90 96 62 Z" fill="var(--gold-tint)" role="img" aria-label="Gold floral branch framing the left side"/>
      <path d="M258 200 Q290 160 322 150 Q332 180 318 200 Q290 222 262 222 Z" fill="var(--gold-tint)" role="img" aria-label="Gold flowers and leaves at the lower right"/>
      <rect x="148" y="52" width="112" height="120" rx="10" fill="var(--script-tint)" role="img" aria-label="Hand-lettered Thank you script in grey"/>
      <circle cx="317" cy="83" r="31" fill="var(--paper)" stroke="url(#gold-sheen)" stroke-width="1.2"/>
      <text x="317" y="85.5" font-family="Montserrat, sans-serif" font-weight="500" font-size="6.2" text-anchor="middle" fill="var(--gold-deep)">SOAK AND SUDS</text>
    </svg>
    <p class="card-message">For Your<br>Purchase And Supporting<br>My Small Business</p>
  </section>

</main>
</body>
</html>
```